Powerpoint template

I am looking for a brand based PPT template that can also be used as the basis for datasheet creation. I have attached a document with some of our branding structure in as an FYI to help.

To be clear I am looking a background design, bullets, layouts, different styles for differing content types. This is a template to be used for lots of presentations.
Updates

Project Deadline Extended
Reason: I have committed to the payment and wanted to give people chance to respond.

Target Market(s)

Enterprise

Requirements
Must have
• Brand standard. different page design choices for different content types
Nice to have
• brand font if it works. Use of some play on the logo in bullets
Should not have
• must be on brand and focused on the business audience

```html
<!DOCTYPE html>
<html lang="en">
<head>
<meta charset="utf-8">
<title>Veranta presentation template</title>
<link href="https://fonts.googleapis.com/css2?family=Open+Sans:wght@400;600;700&display=swap" rel="stylesheet">
<style>
:root{
  --stage:#000;
  --paper:#fff;
  --green:#7cb83e;
  --blue:#1e6cb3;
  --navy:#0d3f6e;
  --navy-deep:#0a2b50;
  --navy-mid:#1a5d93;
  --ink:#444;
  --body:#5a5a5a;
  --sky:#6cb4e8;
  --olive:#6e7f12;
  --amber:#d99a12;
  --icon-light:#f4f6f8;
  --icon-shade:#c9d0d7;
}
*{margin:0;padding:0;box-sizing:border-box}
html,body{width:1200px;height:1000px;overflow:hidden;background:var(--stage)}
body{position:relative;font-family:"Open Sans",Arial,sans-serif;font-variant-emoji:text}
.slide{position:absolute;width:500px;height:375px;background:var(--paper);overflow:hidden}
.slide--pie{left:64px;top:67px}
.slide--bar{left:625px;top:67px}
.slide--icons{left:64px;top:526px}
.slide--contact{left:625px;top:526px}
.slide__title{position:absolute;left:34px;top:17px;font-size:26px;font-weight:700;color:var(--green);letter-spacing:-.2px;white-space:nowrap}
.slide__title .accent{color:var(--blue)}
.slide__rule{position:absolute;left:110px;top:64px;width:290px;height:6px;background:radial-gradient(ellipse at center top,rgba(0,0,0,.22),rgba(0,0,0,0) 70%)}
.heading{position:absolute;display:flex;align-items:center;gap:7px;font-size:12px;font-weight:700;color:var(--ink)}
.bubble{display:inline-flex;align-items:center;justify-content:center;width:18px;height:18px;border-radius:50%;background:radial-gradient(circle at 40% 30%,var(--icon-light),var(--icon-shade));box-shadow:0 1px 2px rgba(0,0,0,.35);color:var(--navy);font-size:10px;font-weight:700;line-height:1}
.copy{position:absolute;left:34px;width:193px;font-size:9.2px;line-height:13.4px;color:var(--body);text-align:justify}
.copy p+p{margin-top:13.4px}
.wave{position:absolute;left:0;top:255px;width:500px;height:120px}
.foot{position:absolute;color:#fff;font-size:6px;line-height:8px}
.foot-link{position:absolute;display:flex;align-items:center;gap:6px;color:#fff;font-size:6px;white-space:nowrap}
.foot-link .dot{width:13px;height:13px;border-radius:50%;background:rgba(255,255,255,.14);display:inline-flex;align-items:center;justify-content:center;font-size:8px;font-weight:700}
.brand{position:absolute;left:378px;top:297px;display:flex;align-items:center;gap:5px;color:#fff;font-size:20px;font-weight:400;letter-spacing:-.3px}
.brand__mark{width:14px;height:14px;border-radius:50%;background:#fff}
.pager{position:absolute;left:384px;top:340px;width:94px;display:flex;align-items:center;justify-content:space-between;color:#fff;font-size:8px}
.pager__btn{width:16px;height:12px;border-radius:6px;background:rgba(255,255,255,.18);display:inline-flex;align-items:center;justify-content:center;font-size:8px;font-weight:700}
.pager em{font-weight:700}
.label{position:absolute;font-size:10px;color:#333;white-space:nowrap}
.legend{position:absolute;display:flex;gap:14px;font-size:7.5px;color:var(--navy)}
.legend span{display:flex;align-items:center;gap:3px}
.legend i{display:inline-block;width:5px;height:5px}
.sw-navy{background:var(--navy)}.sw-sky{background:var(--sky)}.sw-olive{background:var(--olive)}.sw-amber{background:var(--amber)}
.checks{position:absolute;left:272px;top:163px;list-style:none;font-size:8.6px;font-weight:700;color:var(--navy)}
.checks li{height:20.6px;display:flex;align-items:center;gap:5px}
.checks li::before{content:"\2713";font-size:10px}
.icon-grid{position:absolute;left:280px;top:96px;display:grid;grid-template-columns:repeat(6,20px);column-gap:11.6px;row-gap:8.5px}
.icon-grid .bubble{width:20px;height:20px;font-size:11px}
.map{position:absolute;left:33px;top:89px;width:194px;height:98px;background:linear-gradient(120deg,#a9bccb 0%,#b9c7cf 45%,#d8dccf 55%,#cfd6c7 100%)}
.map-shadow{position:absolute;left:55px;top:190px;width:150px;height:12px;background:radial-gradient(ellipse at center,rgba(0,0,0,.35),rgba(0,0,0,0) 70%)}
.contact-item{position:absolute;display:flex;gap:8px;font-size:9.4px;color:var(--body);line-height:14px}
.contact-item strong{display:block;color:var(--ink);font-weight:700}
</style>
</head>
<body>

<!-- Pie chart slide -->
<section class="slide slide--pie">
  <h1 class="slide__title">Pie Chart Example</h1>
  <div class="slide__rule"></div>
  <div class="heading" style="left:30px;top:85px"><span class="bubble">↗</span>Lorem ipsum dolor sit amet</div>
  <div class="copy" style="top:116px">
    <p>consetetur sadipscing elitr, sed diam nonumy eirmod tempor invidunt ut labore et dolore magna aliquyam erat, sed diam voluptua.</p>
    <p>Stet clita kasd gubergren, no sea takimata sanctus est Lorem ipsum dolor sit amet. Lorem ipsum dolor sit amet, consetetur sadipscing elitr, sed diam nonumy eirmod tempor invidunt ut labore et dolore dolores et ea rebum. Stet clita kasd gubergren, no sea takimata sanctus est Lorem ipsum dolor sit amet.</p>
  </div>
  <svg class="pie" style="position:absolute;left:270px;top:140px" width="200" height="120" viewBox="-100 -55 200 120" role="img" aria-label="Pie chart: Nimbus 49, Corvid 31, Helio 13, Other 7">
    <path d="M90,0 A90,45 0 0 1 5.7,44.9 L5.7,64.9 A90,45 0 0 0 90,20 Z" fill="#082c4f"/>
    <path d="M5.7,44.9 A90,45 0 0 1 -90,0 L-90,20 A90,45 0 0 0 5.7,64.9 Z" fill="#3d7fb3"/>
    <path d="M0,0 L0,-45 A90,45 0 0 1 5.7,44.9 Z" fill="var(--navy)"/>
    <path d="M0,0 L5.7,44.9 A90,45 0 0 1 -85.6,-13.9 Z" fill="var(--sky)"/>
    <path d="M0,0 L-85.6,-13.9 A90,45 0 0 1 -38.3,-40.7 Z" fill="var(--olive)"/>
    <path d="M0,0 L-38.3,-40.7 A90,45 0 0 1 0,-45 Z" fill="var(--amber)"/>
  </svg>
  <div class="label" style="left:425px;top:95px;font-size:12px;font-weight:700;color:var(--navy)">49 %</div>
  <div class="label" style="left:428px;top:112px;font-size:7px;font-weight:700;color:var(--navy)">Nimbus</div>
  <div class="label" style="left:296px;top:103px">13</div>
  <div class="label" style="left:367px;top:103px">7</div>
  <div class="label" style="left:266px;top:239px">31</div>
  <div class="legend" style="left:268px;top:255px"><span><i class="sw-navy"></i>Nimbus</span><span><i class="sw-sky"></i>Corvid</span><span><i class="sw-olive"></i>Helio</span><span><i class="sw-amber"></i>Other</span></div>
  <svg class="wave" viewBox="0 0 500 120" preserveAspectRatio="none" aria-hidden="true"><defs><linearGradient id="waveA" x1="0" y1="0" x2="0" y2="1"><stop offset="0" stop-color="var(--navy-mid)"/><stop offset="1" stop-color="var(--navy-deep)"/></linearGradient></defs><path d="M0,55 C130,70 300,40 500,10 L500,120 L0,120 Z" fill="url(#waveA)"/><path d="M0,55 C130,70 300,40 500,10" fill="none" stroke="#fff" stroke-opacity=".5" stroke-width="1"/></svg>
  <div class="foot" style="left:19px;top:332px">Lorem Ipsum Street 122<br>State, Country<br>Phone&nbsp; 0123 4567 89</div>
  <div class="foot-link" style="left:113px;top:334px"><span class="dot">·</span>friendspace.com/company-name</div>
  <div class="foot-link" style="left:113px;top:359px"><span class="dot">@</span>hello@company-name.com</div>
  <div class="foot-link" style="left:262px;top:306px"><span class="dot">⌂</span>company-name.com</div>
  <div class="foot-link" style="left:262px;top:331px"><span class="dot">·</span>chirper.com/company-name</div>
  <div class="foot-link" style="left:262px;top:356px"><span class="dot">·</span>vidstream.com/company-name</div>
  <div class="brand"><span class="brand__mark"></span>Veranta</div>
  <div class="pager"><span class="pager__btn">‹</span><span>9 <em>of</em> 13</span><span class="pager__btn">›</span></div>
</section>

<!-- Bar chart slide -->
<section class="slide slide--bar">
  <h1 class="slide__title">Bar Chart Example</h1>
  <div class="slide__rule"></div>
  <svg style="position:absolute;left:40px;top:95px" width="180" height="160" viewBox="40 95 180 160" role="img" aria-label="Bar chart: Nimbus 49, Corvid 31, Helio 13, Other 7">
    <polygon points="58,212 96,188 205,208 172,236" fill="#fff" stroke="#bbb" stroke-width="1"/>
    <polygon points="78,128 86,121 108,121 100,128" fill="#2f6aa3"/>
    <polygon points="100,128 108,121 108,203 100,210" fill="#072845"/>
    <rect x="78" y="128" width="22" height="82" fill="var(--navy)"/>
    <polygon points="103,161 111,155 133,155 125,161" fill="#a8d4f3"/>
    <polygon points="125,161 133,155 133,208 125,214" fill="#3f86bd"/>
    <rect x="103" y="161" width="22" height="53" fill="var(--sky)"/>
    <polygon points="128,192 136,186 158,186 150,192" fill="#96a83a"/>
    <polygon points="150,192 158,186 158,218 150,224" fill="#4b5808"/>
    <rect x="128" y="192" width="22" height="32" fill="var(--olive)"/>
    <polygon points="153,208 161,202 181,202 173,208" fill="#f0c04a"/>
    <polygon points="173,208 181,202 181,224 173,230" fill="#a8740a"/>
    <rect x="153" y="208" width="20" height="22" fill="var(--amber)"/>
  </svg>
  <div class="label" style="left:86px;top:94px;font-size:12px;font-weight:700;color:var(--navy)">49</div>
  <div class="label" style="left:118px;top:126px">31</div>
  <div class="label" style="left:141px;top:162px">13</div>
  <div class="label" style="left:168px;top:181px">7</div>
  <div class="legend" style="left:46px;top:270px"><span><i class="sw-navy"></i>Nimbus</span><span><i class="sw-sky"></i>Corvid</span><span><i class="sw-olive"></i>Helio</span><span><i class="sw-amber"></i>Other</span></div>
  <div class="heading" style="left:270px;top:85px"><span class="bubble">↗</span>Bullet points list</div>
  <div class="copy" style="left:274px;top:117px;width:193px">Consetetur sadipscing elitr, sed diam nonumy eirmod tempor invidunt ut.</div>
  <ul class="checks">
    <li>Lorem ipsum dolor sit amet,</li>
    <li>Consetetur sadipscing elitr</li>
    <li>Sed diam nonumy eirmod</li>
    <li>Ut labore et dolore dolores</li>
    <li>Cl kasd guber</li>
    <li>Sanctus est lorem</li>
  </ul>
  <svg class="wave" viewBox="0 0 500 120" preserveAspectRatio="none" aria-hidden="true"><defs><linearGradient id="waveB" x1="0" y1="0" x2="0" y2="1"><stop offset="0" stop-color="var(--navy-mid)"/><stop offset="1" stop-color="var(--navy-deep)"/></linearGradient></defs><path d="M0,55 C130,70 300,40 500,10 L500,120 L0,120 Z" fill="url(#waveB)"/><path d="M0,55 C130,70 300,40 500,10" fill="none" stroke="#fff" stroke-opacity=".5" stroke-width="1"/></svg>
  <div class="foot" style="left:19px;top:332px">Lorem Ipsum Street 122<br>State, Country<br>Phone&nbsp; 0123 4567 89</div>
  <div class="foot-link" style="left:113px;top:334px"><span class="dot">·</span>friendspace.com/company-name</div>
  <div class="foot-link" style="left:113px;top:359px"><span class="dot">@</span>hello@company-name.com</div>
  <div class="foot-link" style="left:262px;top:306px"><span class="dot">⌂</span>company-name.com</div>
  <div class="foot-link" style="left:262px;top:331px"><span class="dot">·</span>chirper.com/company-name</div>
  <div class="foot-link" style="left:262px;top:356px"><span class="dot">·</span>vidstream.com/company-name</div>
  <div class="brand"><span class="brand__mark"></span>Veranta</div>
  <div class="pager"><span class="pager__btn">‹</span><span>10 <em>of</em> 13</span><span class="pager__btn">›</span></div>
</section>

<!-- Icon set slide -->
<section class="slide slide--icons">
  <h1 class="slide__title"><span class="accent">Bonus:</span> Over 30 Project Icons</h1>
  <div class="slide__rule"></div>
  <div class="heading" style="left:30px;top:85px"><span class="bubble">+</span>Lorem ipsum dolor sit amet</div>
  <div class="copy" style="top:116px">
    <p>consetetur sadipscing elitr, sed diam nonumy eirmod tempor invidunt ut labore et dolore magna aliquyam erat, sed diam voluptua.</p>
    <p>Stet clita kasd gubergren, no sea takimata sanctus est Lorem ipsum dolor sit amet. Lorem ipsum dolor sit amet, consetetur sadipscing elitr, sed diam nonumy eirmod tempor invidunt ut labore et dolore dolores et ea rebum. Stet clita kasd gubergren, no sea takimata sanctus est Lorem ipsum dolor sit amet.</p>
  </div>
  <div class="icon-grid">
    <span class="bubble"></span><span class="bubble">↓</span><span class="bubble">←</span><span class="bubble">→</span><span class="bubble">↑</span><span class="bubble">‹</span>
    <span class="bubble">…</span><span class="bubble">✕</span><span class="bubble">$</span><span class="bubble">€</span><span class="bubble">!</span><span class="bubble"></span>
    <span class="bubble">⌂</span><span class="bubble">▯</span><span class="bubble">▮</span><span class="bubble">♥</span><span class="bubble">✉</span><span class="bubble">@</span>
    <span class="bubble">⚲</span><span class="bubble">−</span><span class="bubble">▭</span><span class="bubble">›</span><span class="bubble">✓</span><span class="bubble">☎</span>
    <span class="bubble">+</span><span class="bubble">▣</span><span class="bubble">?</span><span class="bubble">≈</span><span class="bubble">☺</span><span class="bubble">↗</span>
    <span class="bubble">✓</span><span class="bubble"></span><span class="bubble">♙</span><span class="bubble">▤</span><span class="bubble">⊕</span><span class="bubble"></span>
  </div>
  <svg class="wave" viewBox="0 0 500 120" preserveAspectRatio="none" aria-hidden="true"><defs><linearGradient id="waveC" x1="0" y1="0" x2="0" y2="1"><stop offset="0" stop-color="var(--navy-mid)"/><stop offset="1" stop-color="var(--navy-deep)"/></linearGradient></defs><path d="M0,55 C130,70 300,40 500,10 L500,120 L0,120 Z" fill="url(#waveC)"/><path d="M0,55 C130,70 300,40 500,10" fill="none" stroke="#fff" stroke-opacity=".5" stroke-width="1"/></svg>
  <div class="foot" style="left:19px;top:332px">Lorem Ipsum Street 122<br>State, Country<br>Phone&nbsp; 0123 4567 89</div>
  <div class="foot-link" style="left:113px;top:334px"><span class="dot">·</span>friendspace.com/company-name</div>
  <div class="foot-link" style="left:113px;top:359px"><span class="dot">@</span>hello@company-name.com</div>
  <div class="foot-link" style="left:262px;top:306px"><span class="dot">⌂</span>company-name.com</div>
  <div class="foot-link" style="left:262px;top:331px"><span class="dot">·</span>chirper.com/company-name</div>
  <div class="foot-link" style="left:262px;top:356px"><span class="dot">·</span>vidstream.com/company-name</div>
  <div class="brand"><span class="brand__mark"></span>Veranta</div>
  <div class="pager"><span class="pager__btn">‹</span><span>11 <em>of</em> 13</span><span class="pager__btn">›</span></div>
</section>

<!-- Contact slide -->
<section class="slide slide--contact">
  <h1 class="slide__title">Contact Page</h1>
  <div class="map" role="img" aria-label="Map showing the office location"></div>
  <div class="map-shadow"></div>
  <div class="contact-item" style="left:30px;top:215px"><span class="bubble">⚲</span><div><strong>Address</strong>Lorem Ipsum Street 122<br>State, Country</div></div>
  <div class="contact-item" style="left:30px;top:268px"><span class="bubble">☎</span><div><strong>Phone</strong>0123 4567 89</div></div>
  <div class="contact-item" style="left:270px;top:59px"><span class="bubble">⌂</span><div><strong>Website</strong>company-name.com</div></div>
  <div class="contact-item" style="left:270px;top:101px"><span class="bubble">@</span><div><strong>E-Mail</strong>hello@company-name.com</div></div>
  <div class="contact-item" style="left:270px;top:144px"><span class="bubble"></span><div><strong>Friendspace</strong>friendspace.com/company-name</div></div>
  <div class="contact-item" style="left:270px;top:185px"><span class="bubble"></span><div><strong>Chirper</strong>chirper.com/company-name</div></div>
  <div class="contact-item" style="left:270px;top:227px"><span class="bubble"></span><div><strong>Vidstream</strong>vidstream.com/company-name</div></div>
  <svg class="wave" viewBox="0 0 500 120" preserveAspectRatio="none" aria-hidden="true"><defs><linearGradient id="waveD" x1="0" y1="0" x2="0" y2="1"><stop offset="0" stop-color="var(--navy-mid)"/><stop offset="1" stop-color="var(--navy-deep)"/></linearGradient></defs><path d="M0,55 C130,70 300,40 500,10 L500,120 L0,120 Z" fill="url(#waveD)"/><path d="M0,55 C130,70 300,40 500,10" fill="none" stroke="#fff" stroke-opacity=".5" stroke-width="1"/></svg>
  <div class="foot" style="left:19px;top:332px">Lorem Ipsum Street 122<br>State, Country<br>Phone&nbsp; 0123 4567 89</div>
  <div class="foot-link" style="left:113px;top:334px"><span class="dot">·</span>friendspace.com/company-name</div>
  <div class="foot-link" style="left:113px;top:359px"><span class="dot">@</span>hello@company-name.com</div>
  <div class="foot-link" style="left:262px;top:306px"><span class="dot">⌂</span>company-name.com</div>
  <div class="foot-link" style="left:262px;top:331px"><span class="dot">·</span>chirper.com/company-name</div>
  <div class="foot-link" style="left:262px;top:356px"><span class="dot">·</span>vidstream.com/company-name</div>
  <div class="brand"><span class="brand__mark"></span>Veranta</div>
  <div class="pager"><span class="pager__btn">‹</span><span>12 <em>of</em> 13</span><span class="pager__btn">›</span></div>
</section>

</body>
</html>
```